July 2022 Industrial Manufacturer Product Expo Mexico City

We manufacture large screws and fastners for large Mining equipment, Trains, large ships, airplanes, wind turbines, and so on. We also do custom work base on the customer needs. No matter the size we can make it.
We have a Expo coming up with companies all over the world. We have to stand out we are a family own business so our customer service will be above and beyond anyone can provide. We do not have a sales force to push our products and services we provide one on one service.
Plus@!! I'm looking for anything that you designers can come up with if it was your company to put on a business card, plus i want to do a 1 or 2 sided pamphlet, and then a website. We make Speciality Bolts for large mining equipment these bolts can be 3 to 4 foot long!!! Plus fasteners, Nuts, washers, any, size, strengths, special materials, we offer more of a ono on one customer service, We are a small company, family own, but can fulfill any type of orders. We can also provide special time lines for emergency orders. "We keep the machines running we here at RWK don't believe in down time" We want to hear any slogan based on our company to stand out.
Thanks i really appreciate all your work and options that we have to pick on. Plus just a thought we could possibly want to entertain a experience Marketing internet help maybe a employment possibility. Thanks
Updates

I need 2 cards one in Spanish and English Like the steel back ground maybe send me in some bright red and blue writing Same with the Black cards Please remove the word Military The logo RWK maybe integrate a picture of a Bolt 🔩 Thank you

Still looking for I need 2 cards one in Spanish and English Like the steel back ground maybe send me in some bright red and blue writing Same with the Black cards try bright writing Please remove the word Military The logo RWK maybe integrate a picture of a Bolt 🔩 Plus will need the company to make a brochure and website next Thank you

Target Market(s)

Large Mining, Ship, Train, Green Energy, OPRE, and Government equipment. Throughout the World

Industry/Entity Type

We can Custom Manufacture any type of Fastners for Mining equipment, Trains, Ships, Green energy, Governments, or military projects. wind turbines,

Contact Information for Business Card

I attached the name and contact info that's on a card, plus the Company Logo. Would like industrial looking background with Bright Colors that will stand out!! If we can insert somewhere maybe on back that we "Custom Manufacture Any Size or Quantity Fastners for Large Mining Equipment, Trains, Ships, Green Energy Equipment or Government Projects

Font styles to use
Other font styles liked:
• You Pick, has to be bold, colorful standout, Professional looking Beable to read it.

Colors

Designer to choose colors to be used in the design.

Requirements
Must have
• Need in Spanish and English TO STANDOUT FROM THE REST OF THE EXPO!! See Business card details, Rounded corners
Nice to have
• Can i see some of the darker cards with Bright Red and Blue letters I like to see the different type of card material, heavy thickness, plastic, transparent, Metal types, Bright Colors, I saw like Raised letters like on the logo.

```html
<!DOCTYPE html>
<html lang="es">
<head>
<meta charset="utf-8">
<title>RWK – Tarjeta de presentación</title>
<link rel="stylesheet" href="https://fonts.googleapis.com/css2?family=Roboto+Condensed:wght@400;700&display=swap">
<style>
  :root {
    --backdrop: #9a9a9a;
    --card-white: #f6f6f6;
    --card-black: #1f1f1f;
    --edge-blue: #1e8fe0;
    --name-dark: #2b3a8c;
    --name-light: #1f8fd6;
    --ink-gray: #555555;
    --icon-blue: #2d62c9;
    --divider: #b5b5b5;
    --logo-silver: #d9d9d9;
    --tagline: #e8e8e8;
  }
  * { box-sizing: border-box; margin: 0; padding: 0; }
  html, body {
    width: 1200px; height: 1050px; overflow: hidden;
    background: var(--backdrop);
    font-family: "Roboto Condensed", Arial, sans-serif;
  }
  .canvas {
    width: 1200px; height: 1050px;
    display: flex; flex-direction: column; align-items: center; justify-content: center;
    gap: 60px;
  }
  .card {
    width: 700px; height: 400px;
    border-radius: 14px;
    border-bottom: 5px solid var(--edge-blue);
    position: relative;
    overflow: hidden;
  }
  .card--front { background: var(--card-white); }
  .card--back { background: var(--card-black); }

  /* Front */
  .identity {
    position: absolute; right: 372px; top: 170px;
    text-align: right;
  }
  .identity__name {
    font-size: 24px; font-weight: 700; white-space: nowrap;
    letter-spacing: 0.2px;
  }
  .identity__name .title, .identity__name .first { color: var(--name-dark); }
  .identity__name .middle { color: var(--name-light); }
  .identity__name .last { color: var(--name-dark); }
  .identity__role {
    margin-top: 4px; font-size: 16px; color: var(--ink-gray);
  }
  .divider {
    position: absolute; left: 350px; top: 168px;
    width: 1px; height: 72px; background: var(--divider);
  }
  .contact {
    position: absolute; left: 372px; top: 178px;
    list-style: none;
    font-size: 16px; color: var(--ink-gray); line-height: 22px;
  }
  .contact li { display: flex; align-items: center; gap: 8px; }
  .contact svg { width: 14px; height: 14px; fill: var(--icon-blue); flex: none; }

  /* Back */
  .brand {
    position: absolute; left: 0; right: 0; top: 112px;
    text-align: center;
  }
  .brand__name {
    font-size: 120px; font-weight: 700; line-height: 1;
    color: var(--logo-silver); letter-spacing: 10px;
  }
  .brand__tagline {
    margin-top: 18px;
    font-size: 24px; font-weight: 400; letter-spacing: 1px;
    color: var(--tagline);
  }
</style>
</head>
<body>
<main class="canvas">
  <section class="card card--front" aria-label="Frente de la tarjeta">
    <div class="identity">
      <p class="identity__name">
        <span class="title">Lic.</span>
        <span class="first">Mariela</span>
        <span class="middle">Soto</span>
        <span class="last">Vargas</span>
      </p>
      <p class="identity__role">Cotizaciones en</p>
    </div>
    <div class="divider"></div>
    <ul class="contact">
      <li>
        <svg viewBox="0 0 24 24" aria-hidden="true"><path d="M6.6 10.8a15.1 15.1 0 0 0 6.6 6.6l2.2-2.2a1 1 0 0 1 1-.25 11.4 11.4 0 0 0 3.6.57 1 1 0 0 1 1 1V20a1 1 0 0 1-1 1A17 17 0 0 1 3 4a1 1 0 0 1 1-1h3.5a1 1 0 0 1 1 1c0 1.25.2 2.45.57 3.57a1 1 0 0 1-.25 1z"/></svg>
        5550142301
      </li>
      <li>
        <svg viewBox="0 0 24 24" aria-hidden="true"><path d="M7 2h10a2 2 0 0 1 2 2v16a2 2 0 0 1-2 2H7a2 2 0 0 1-2-2V4a2 2 0 0 1 2-2zm0 3v13h10V5z"/></svg>
        5550189420
      </li>
      <li>
        <svg viewBox="0 0 24 24" aria-hidden="true"><path d="M2 5h20v14H2zm2 2v.5l8 5 8-5V7zm0 3v7h16v-7l-8 5z"/></svg>
        rwk.ventas@correo.com
      </li>
    </ul>
  </section>

  <section class="card card--back" aria-label="Reverso de la tarjeta">
    <div class="brand">
      <p class="brand__name">RWK</p>
      <p class="brand__tagline">FABRICACION Y DISTRIBUCION DE TORNILLOS</p>
    </div>
  </section>
</main>
</body>
</html>
```